International MultiIndustry Team Coaching Site

Hello Designers,
We need a redesign of the pages attached.
The design must be engaging and modern, with a focus on the user experience, particularly for the "observations" page. Because this is the main page of the website. It is to be used on a 10'' tablet or desktop, to record observations on the fly, so it must be intuitive and efficient.
The positioning of the metrics and observations and etc, are just a reference. you can switch it up if you feel there is a better way (PLEASE DO ;) ).

There are many categories (color coded with borders in the example hpt_6_observations.jpg) and observation metrics within each category. This is the Key page, because it is the One with the most interactions.

The user should know when it has selected a category (there should be some visual hint) and the different metric widgets should be accounted for.
There are 3: The time widget at the end, numerical widgets (recording more or less numbers), and boolean ones (selected or not).

For the numerical widgets, we show plus and minus characters, but you can change this, being creative, keeping in mind that it must work well on a mobile device and desktop, and must be intuitive and quick.

Set your creativity free with the login screen , home screen, categories secret, events screen, journaling and observations screen .

We would like the site/mobile version to have a very modern look. Something that would be found in very popular and user friendly apps.

***** The events, journaling, category and home screens are getting 2 much attention , please focus also on the observations screen *******
Imagine you are a psychologist tasked with observing the behaviour of teenagers during group work. And you have a tablet on which to record what you observe. Now imagine you need to observe during 3 classes: Biology, Math, Physics (these are events). For each class (event) you will have to record observations in 3 categories: Social Interaction, Leadership, Communication (these are categories).
Example of the metrics (these are observations) for Leadership:
" the teenager direct other colleagues" (boolean widget),
"the teenager speaks more than everyone else" (boolean widget)
"the teenager interrupts colleagues speaking" (number widget)
"the work took hh:mm" (time widget)

The observations screen can have any shape and form you think of. It doesn't need to be that single column with yes and nos, or that double column with the squared cards.
thank you.

Hope that was useful intel :)
Available for any questions you might have.
Good luck :)

Target Market(s)

Enterprise teams

Number of Pages Required

5+ page

Font styles to use
Sans Serif

Requirements
Must have
• Modern design

```html
<!DOCTYPE html>
<html lang="en">
<head>
<meta charset="utf-8">
<title>Team Coaching Dashboard</title>
<link href="https://fonts.googleapis.com/css2?family=Poppins:wght@400;500;600&display=swap" rel="stylesheet">
<style>
:root{
  --ink:#1f1f24;
  --muted:#555;
  --line:#e4e4ea;
  --accent:#4b3f8f;
  --brand-blue:#3e6fb8;
  --rose:#b8355f;
  --page:#f7f7f9;
  --card:#ffffff;
  --green:#3ccf4e;
  --sky:#3a8ee6;
  --red:#e0262c;
  --map:#e6e6ec;
}
*{box-sizing:border-box;margin:0;padding:0}
html,body{width:1200px;height:703px;overflow:hidden}
body{font-family:'Poppins',sans-serif;color:var(--ink);background:#fff;position:relative}
.abs{position:absolute}
.header{left:0;top:0;width:1200px;height:77px;background:#fff;box-shadow:0 2px 10px rgba(0,0,0,.05);z-index:3}
.brand{left:52px;top:30px;font-weight:600;font-size:15px;color:var(--brand-blue)}
.search{left:177px;top:20px;width:313px;height:41px;border:1px solid #9a9aa2;border-radius:21px;display:flex;align-items:center;padding-left:16px;gap:14px;font-size:13px;color:#8a8a92}
.icon{top:32px}
.badge{left:927px;top:21px;width:14px;height:14px;border-radius:50%;background:var(--rose);color:#fff;font-size:8px;text-align:center;line-height:14px}
.divider{left:997px;top:0;width:1px;height:77px;background:#bbb}
.avatar{left:1017px;top:26px;width:36px;height:36px;border-radius:50%;background:linear-gradient(135deg,#c9a98a,#6f7f6a)}
.welcome-user{left:1062px;top:35px;font-size:13px;color:var(--ink);display:flex;align-items:center;gap:4px}
.welcome-user b{color:var(--rose);font-weight:600}
.sidebar{left:0;top:77px;width:163px;height:609px;background:#fff;box-shadow:2px 0 8px rgba(0,0,0,.04);z-index:2}
.nav{list-style:none;position:absolute;left:14px;top:38px}
.nav li{display:flex;align-items:center;gap:8px;font-size:11.5px;color:#444;height:26.3px}
.nav li.active{color:var(--brand-blue)}
.main{left:163px;top:77px;width:1037px;height:609px;background:var(--page)}
.page-title{left:177px;top:86px;font-size:16px;font-weight:600}
.card{background:var(--card);box-shadow:0 2px 8px rgba(0,0,0,.05)}
.tile{top:120px;width:238px;height:82px;padding:14px 15px}
.tile h3{font-size:14px;font-weight:500;line-height:1.3}
.tile p{font-size:10px;color:var(--muted);line-height:1.7;margin-top:4px}
.tile .date{font-size:11.5px;color:#333;margin-top:4px}
.add{display:flex;align-items:center;justify-content:center;gap:10px;color:var(--accent);font-weight:500;font-size:14.5px}
.panel{top:216px;height:305px}
.panel h2{position:absolute;font-size:16px;font-weight:500;top:20px}
.team{top:387px;width:238px;height:82px;padding:12px 25px}
.team h4{font-size:14px;font-weight:500}
.team p{font-size:9px;color:#444;line-height:1.9;margin-top:6px}
.team .tools{position:absolute;right:8px;top:11px;display:flex;gap:6px}
.map{left:862px;top:291px;width:298px;height:149px;background:radial-gradient(ellipse at 50% 40%,var(--map) 40%,#f2f2f5 75%,#fff 100%);border-radius:40px}
.zoom{left:869px;width:9px;height:9px;background:#333;border-radius:2px;color:#fff;font-size:8px;line-height:9px;text-align:center}
.menu{left:1050px;top:78px;width:123px;height:102px;background:#fff;box-shadow:0 3px 12px rgba(0,0,0,.1);border-radius:3px;z-index:4;font-size:10px;color:#333}
.menu .item{position:absolute;left:16px;display:flex;align-items:center;gap:7px}
.menu hr{position:absolute;left:4px;right:4px;top:64px;border:0;border-top:1px solid var(--line)}
</style>
</head>
<body>

<header class="abs header">
  <div class="abs brand">Teamwise</div>
  <div class="abs search">
    <svg width="18" height="18" viewBox="0 0 18 18" fill="none" stroke="#333" stroke-width="2"><circle cx="8" cy="8" r="6.5"/><path d="M13 13l4 4"/></svg>
    Enter Keyword
  </div>
  <div class="abs icon" role="img" aria-label="Language flag" style="left:810px;top:36px;width:21px;height:12px;background:linear-gradient(180deg,#2a3f8a,#c8283a 50%,#2a3f8a)"></div>
  <svg class="abs icon" style="left:849px" width="14" height="14" viewBox="0 0 14 14" fill="none" stroke="#555"><rect x="1" y="2" width="12" height="11" rx="1"/><path d="M1 5h12M4 1v2M10 1v2"/></svg>
  <svg class="abs icon" style="left:888px" width="13" height="13" viewBox="0 0 13 13" fill="none" stroke="#555"><rect x="1" y="1" width="4.5" height="4.5"/><rect x="7.5" y="1" width="4.5" height="4.5"/><rect x="1" y="7.5" width="4.5" height="4.5"/><rect x="7.5" y="7.5" width="4.5" height="4.5"/></svg>
  <svg class="abs icon" style="left:920px" width="14" height="15" viewBox="0 0 14 15" fill="#444"><path d="M7 1a4 4 0 0 0-4 4v4L1 11v1h12v-1l-2-2V5a4 4 0 0 0-4-4zM5.5 13a1.5 1.5 0 0 0 3 0z"/></svg>
  <div class="abs badge">5</div>
  <svg class="abs icon" style="left:954px" width="15" height="15" viewBox="0 0 15 15" fill="none" stroke="#555"><circle cx="7.5" cy="7.5" r="2.3"/><circle cx="7.5" cy="7.5" r="5.8" stroke-dasharray="2.5 1.5"/></svg>
  <div class="abs divider"></div>
  <div class="abs avatar" role="img" aria-label="User profile photo"></div>
  <div class="abs welcome-user">Welcome <b>Rowan</b>
    <svg width="12" height="8" viewBox="0 0 12 8" fill="none" stroke="#222" stroke-width="1.5"><path d="M1 1l5 5 5-5"/></svg>
  </div>
</header>

<div class="abs menu">
  <div class="item" style="top:10px">
    <svg width="10" height="10" viewBox="0 0 10 10"><circle cx="5" cy="5" r="4.5" fill="#333"/><circle cx="5" cy="4" r="1.6" fill="#fff"/></svg>Profile</div>
  <div class="item" style="top:37px">
    <svg width="10" height="10" viewBox="0 0 10 10" fill="#333"><rect x="1.5" y="4.5" width="7" height="5"/><path d="M3 4.5V3a2 2 0 0 1 4 0v1.5" fill="none" stroke="#333"/></svg>Lock Screen</div>
  <hr>
  <div class="item" style="top:77px">
    <svg width="10" height="10" viewBox="0 0 10 10" fill="none" stroke="#333"><path d="M6 1H1v8h5M4 5h5M7 3l2 2-2 2"/></svg>Logout</div>
</div>

<aside class="abs sidebar">
  <ul class="nav">
    <li class="active"><svg width="13" height="13" viewBox="0 0 13 13" fill="none" stroke="#3e6fb8"><path d="M1 6l5.5-5 5.5 5M2.5 5v7h8V5"/></svg>Home</li>
    <li><svg width="13" height="13" viewBox="0 0 13 13" fill="none" stroke="#777"><rect x="1" y="2" width="11" height="10"/><path d="M1 5h11"/></svg>Event &amp; Listing</li>
    <li><svg width="13" height="13" viewBox="0 0 13 13" fill="none" stroke="#555"><rect x="1" y="1" width="4.5" height="4.5"/><rect x="7.5" y="1" width="4.5" height="4.5"/><rect x="1" y="7.5" width="4.5" height="4.5"/><rect x="7.5" y="7.5" width="4.5" height="4.5"/></svg>Category Listing</li>
    <li><svg width="13" height="13" viewBox="0 0 13 13" fill="none" stroke="#777"><rect x="1" y="1" width="11" height="11" rx="2"/><path d="M4 5h5M4 8h5"/></svg>Observation Listing</li>
    <li><svg width="13" height="13" viewBox="0 0 13 13" fill="none" stroke="#777"><circle cx="6.5" cy="6.5" r="2"/><path d="M1 6.5C3 3 10 3 12 6.5 10 10 3 10 1 6.5"/></svg>Hpt Observations</li>
    <li><svg width="13" height="13" viewBox="0 0 13 13" fill="none" stroke="#999"><rect x="1" y="1" width="11" height="11"/><circle cx="6.5" cy="6.5" r="2"/></svg>Observations with...</li>
  </ul>
</aside>

<main class="abs main"></main>

<div class="abs page-title">Welcome</div>

<div class="abs card tile add" style="left:171px">
  <svg width="18" height="18" viewBox="0 0 18 18" fill="#4b3f8f"><rect x="7.5" y="0" width="3" height="18"/><rect x="0" y="7.5" width="18" height="3"/></svg>
  Add New Narrative
</div>
<div class="abs card tile" style="left:426px">
  <h3>My Journaling</h3>
  <p>Lorem Ipsum is simply dummy text<br>of the printing and typesetting</p>
</div>
<div class="abs card tile" style="left:679px">
  <h3>Hpt Observations</h3>
  <div class="date">8 Feb 2023</div>
</div>
<div class="abs card tile" style="left:934px">
  <h3>Observations with<br>dessign</h3>
  <div class="date" style="margin-top:2px">02 Feb 2023</div>
</div>

<section class="abs card panel" style="left:171px;width:662px">
  <h2 style="left:28px">All Teams</h2>
</section>
<div class="abs card add" style="left:198px;top:287px;width:238px;height:82px">
  <svg width="18" height="18" viewBox="0 0 18 18" fill="#4b3f8f"><rect x="7.5" y="0" width="3" height="18"/><rect x="0" y="7.5" width="18" height="3"/></svg>
  Add New Team
</div>

<div class="abs card team" style="left:198px">
  <h4>Grass Team</h4>
  <p>Lorem Ipsum is simply dummy text of the<br>printing and typesetting industry.</p>
  <div class="tools">
    <svg width="14" height="17" viewBox="0 0 14 17" fill="none" stroke="#3ccf4e"><path d="M1 1h8l4 4v11H1z"/><path d="M4 12c2-5 4-5 6 0"/></svg>
    <svg width="19" height="17" viewBox="0 0 19 17" fill="none" stroke="#3a8ee6"><path d="M1 1v15h17"/><path d="M3 14c3 0 4-11 7-11s3 11 7 11" /></svg>
    <svg width="14" height="17" viewBox="0 0 14 17" fill="none" stroke="#e0262c" stroke-width="1.4"><path d="M1 3h12M5 3V1h4v2M2 3l1 13h8l1-13M5 6v8M7 6v8M9 6v8"/></svg>
  </div>
</div>
<div class="abs card team" style="left:456px">
  <h4>Hard Court</h4>
  <p>Lorem Ipsum is simply dummy text of the<br>printing and typesetting industry.</p>
  <div class="tools">
    <svg width="14" height="17" viewBox="0 0 14 17" fill="none" stroke="#3ccf4e"><path d="M1 1h8l4 4v11H1z"/><path d="M4 12c2-5 4-5 6 0"/></svg>
    <svg width="19" height="17" viewBox="0 0 19 17" fill="none" stroke="#3a8ee6"><path d="M1 1v15h17"/><path d="M3 14c3 0 4-11 7-11s3 11 7 11" /></svg>
    <svg width="14" height="17" viewBox="0 0 14 17" fill="none" stroke="#e0262c" stroke-width="1.4"><path d="M1 3h12M5 3V1h4v2M2 3l1 13h8l1-13M5 6v8M7 6v8M9 6v8"/></svg>
  </div>
</div>

<section class="abs card panel" style="left:846px;width:325px">
  <h2 style="left:21px">Lets find us</h2>
</section>
<div class="abs zoom" style="top:293px">+</div>
<div class="abs zoom" style="top:306px">−</div>
<div class="abs map" role="img" aria-label="World map with office locations"></div>

</body>
</html>
```